Nobody Left the Lantern Burning - Tom Halvery - CD Cover Design Project

Single Cover for CD & Online media e.g. Tunebox Graphics
The first song release from Tom Halvery will be the track 'Nobody Left the Lantern Burning'.
For the release the single requires artwork that is eye catching, seriously professional & meets the requirements of Disc Sprout, Tunebox and also a physical copy on CD.
Track listings for CD will be:
1. Nobody Left the Lantern Burning
2. Nobody Left the Lantern Burning - Instrumental
see details in this link:
http://members.discsprout-example.com/faq.aspx
http://selfmadesound.discsprout-example.com/2009/11/avoid-album-art-atrocities/
http://answers.quorvex-example.com/question/index?qid=20111015141433AAdDTmH
Any advice on this would be greatly appreciated,
I would also like the two logo's I have uploaded to be used,
one is the Tom Halvery logo and the other is for Milbrook & Tandy Records logo (please remove the R and replace with a C for copyright.)
There are four high res photo shopped pictures of Tom Halvery and another zip file of many others, it would be nice to include one of these maybe on the 2nd page or back of the CD. Please don't use them as the front cover.
I imagine an Art Deco illustration but please listen to the track and let it inspire you.
Good Luck
Updates
I don't feel this is what I'm looking for, the design needs to refelct a broken heart without being a picture of a broken heart
Reason: No design has been what we are after so far so the deadline has been extended and the budget increased.

```html
<!DOCTYPE html>
<html lang="en">
<head>
<meta charset="utf-8">
<title>Nobody Left the Lantern Burning – Tom Halvery</title>
<link rel="stylesheet" href="https://fonts.googleapis.com/css2?family=Fjalla+One&display=swap">
<style>
  :root {
    --paper-red: #f0261c;
    --paper-red-light: #ff3b2e;
    --paper-core: #d9c9a6;
    --void: #050506;
    --text-white: #ffffff;
    --label-maroon: #5a1a24;
    --photo-dark: #1a1410;
    --photo-mid: #6a4a36;
  }
  html, body {
    margin: 0;
    padding: 0;
    width: 1200px;
    height: 1200px;
    overflow: hidden;
    background: var(--void);
  }
  .cover {
    position: relative;
    width: 1200px;
    height: 1200px;
    overflow: hidden;
    background: var(--void);
    font-family: "Fjalla One", "Arial Narrow", sans-serif;
  }
  .artist-photo {
    position: absolute;
    left: 600px;
    top: 230px;
    width: 600px;
    height: 730px;
    background: radial-gradient(ellipse 55% 60% at 55% 45%, var(--photo-mid) 0%, #3b2a20 45%, var(--photo-dark) 75%, var(--void) 100%);
  }
  .torn-paper {
    position: absolute;
    inset: 0;
    width: 1200px;
    height: 1200px;
  }
  .track-list {
    position: absolute;
    left: 40px;
    top: 452px;
    width: 600px;
    margin: 0;
    padding: 0;
    list-style: none;
    text-align: center;
    color: var(--text-white);
    font-size: 33px;
    line-height: 63px;
    letter-spacing: 0.5px;
  }
  .record-label {
    position: absolute;
    right: 22px;
    bottom: 26px;
    display: flex;
    flex-direction: column;
    align-items: center;
    gap: 8px;
    color: var(--label-maroon);
    font-size: 14px;
    letter-spacing: 0.3px;
    text-transform: uppercase;
  }
  .record-label-dot {
    width: 70px;
    height: 70px;
    border-radius: 50%;
    background: var(--label-maroon);
  }
</style>
</head>
<body>
  <main class="cover">
    <div class="artist-photo" role="img" aria-label="Photograph of Tom Halvery looking down, wearing glasses and a white shirt, against a dark background"></div>

    <svg class="torn-paper" viewBox="0 0 1417 1417" aria-hidden="true">
      <defs>
        <linearGradient id="redSheet" x1="0" y1="0" x2="0" y2="1">
          <stop offset="0" stop-color="var(--paper-red-light)"/>
          <stop offset="1" stop-color="var(--paper-red)"/>
        </linearGradient>
      </defs>
      <!-- upper sheet: paper core then red surface -->
      <path fill="var(--paper-core)" d="M0 0 H1417 V385 L1330 372 L1250 392 L1150 362 L1060 312 L980 250 L900 262 L830 302 L760 282 L700 220 L650 242 L580 302 L540 272 L480 202 L420 150 L330 160 L250 140 L140 130 L80 200 L0 250 Z"/>
      <path fill="url(#redSheet)" d="M0 0 H1417 V360 L1330 345 L1250 360 L1160 330 L1070 290 L990 230 L900 235 L830 275 L760 250 L700 200 L650 215 L585 270 L545 240 L485 175 L425 120 L330 125 L255 110 L140 100 L90 160 L0 220 Z"/>
      <!-- lower sheet: paper core then red surface -->
      <path fill="var(--paper-core)" d="M0 1417 H1417 V1025 L1320 1042 L1250 1100 L1150 1095 L1050 1100 L900 1108 L800 1128 L720 1118 L660 1140 L620 1090 L570 1050 L520 1010 L440 990 L370 970 L300 930 L200 918 L90 938 L60 998 L0 1048 Z"/>
      <path fill="url(#redSheet)" d="M0 1417 H1417 V1040 L1325 1058 L1255 1112 L1150 1106 L1050 1110 L900 1116 L800 1136 L720 1126 L662 1148 L618 1098 L568 1056 L518 1016 L440 996 L372 976 L300 936 L200 924 L92 944 L62 1004 L0 1054 Z"/>
    </svg>

    <ol class="track-list">
      <li>1. Nobody Left the Lantern Burning</li>
      <li>2. Nobody Left the Lantern Burning -</li>
      <li>(Instrumental)</li>
    </ol>

    <div class="record-label">
      <span class="record-label-dot"></span>
      <span class="record-label-name">Milbrook &amp; Tandy Records</span>
    </div>
  </main>
</body>
</html>
```